Herb Farm - Tea Label Design

We are a small herbalist company called 'Meadowlark Remedies' which requires a new label scheme.

Meadowlark Remedies specializes in organic wellness teas, handmade soaps, bath and beauty products. We also offer local beeswax, pollen and an herb CSA.

Our slogan is "Timeless Herbs for Gentle Living" and we frequently market ourselves as an "Apothecary & Herb Farm".

The primary use of this label will be on tins and biodegradable food grade paper bags.

We are looking for:

1) An unique universal design for our products. Something that we can put on the tea tins/bags as well as boxes in the future. To keep costs down I would like something that can be used on a variety of products by simply having the colour changed or adding the title of the product in a certain area. We have four collections. Please see the attached style guide. I particularly like the Silverbrook Leaf Co. as each type of tea is reprinted by a design. Please see their website for further clarification. I also really like their styling.

2) Label required is 8.5" x 5.25" (w - h). Bear in mind we also have dark cobalt blue jars and Kraft biodegradable bags available that this label will fit on (5570-02 as pictured)

3) We would like to see a design that is colourful, and has elements of modern simplicity yet certainly has an old world apothecary charm.

4) Please refer to our current label for product information. Not everything has to be in the same place in the new design, however all the information is required.

We will require source files in .ai and .eps (layers retained, no outlines on text, list of fonts used).

Please visit: www.meadowlarkremedies.example

We included a few favourites and the styles we prefer, but please be creative!

The label chosen could be in for a lot more design work as we expand our company. Any other input regarding packaging would be helpful.
Updates

Hello Designers!

I have posted our current label for you to review - I like it, yet I don't. You can see the level of craftsman ship brings up to artisan, and mid-high range product. The only parts I really want to keep from this label is how the brewing instructions are set out.

In terms of design, I do not want to use a photograph on the label - it is there for inspiration!

Thanks,
Meadowlark Remedies 

Reason: I would like to see more designs, from a variety of designers for this label project.

Reason: Would like to see more designs.

Reason: In receiving designs I realized that the sizing is not ideal as it does not have ample space for the required information. I have updated the brief to reflect this and posted a working file that has the required elements. A lot of good designs, but I noticed the over use of filigree or Victorian ornamentation. I would like some ornamentation but simplicity is desired in the overall label. There was not enough designs submitted, nothing that truly wow-ed me. I hope to see more unique designs! Thanks.

Target Market(s)

30-something, retired, eco-conscious, women, mid-priced marketing, local Ontario Canada; some products will be sold at a local historical village

Industry/Entity Type

Biodegradable

Font styles to use
Decorative
Other font styles liked:
• DellaRobbia BT Bold; Foglihten No07

Requirements
Must have
• Fonts used: Dellarobbia BT Bold and Foglihten No07
Use fonts and logo design; you can use separate leaf components but fonts chosen for logo cannot change

Other fonts can be used but please use Foglihten No07 for "Meadowlark Remedies" and Dellarobbia BT Bold for "Apothecary & Herb Farm" and for "Timeless Herbs for Gentle Living".
Nice to have
• "Apothecary & Herb Farm" or slogan
Should not have
• Comic sans
clipart
Filigree or line swooshes

```html
<!DOCTYPE html>
<html lang="en">
<head>
<meta charset="UTF-8">
<title>Meadowlark Remedies – Hillside Collection Label</title>
<link rel="stylesheet" href="https://fonts.googleapis.com/css2?family=Marcellus&family=Della+Respira&display=swap">
<style>
  :root {
    --page: #ffffff;
    --label-cream: #fbf8cf;
    --gold: #e4c23c;
    --gold-soft: #e5d68e;
    --herb-green: #0f7f55;
    --sage-green: #3a9871;
    --bark-brown: #6b3a22;
    --leaf-brown: #7a4a34;
    --leaf-plum: #5a3440;
  }
  * { margin: 0; padding: 0; box-sizing: border-box; }
  html, body {
    width: 1200px;
    height: 1000px;
    overflow: hidden;
    background: var(--page);
  }
  .canvas {
    position: relative;
    width: 1200px;
    height: 1000px;
  }
  .label {
    position: absolute;
    left: 115px;
    top: 185px;
    width: 975px;
    height: 633px;
    background: var(--label-cream);
  }
  .label-lines {
    position: absolute;
    left: 0;
    top: 0;
    width: 1200px;
    height: 1000px;
  }
  .text-line {
    position: absolute;
    left: -4px;
    width: 1200px;
    text-align: center;
    white-space: nowrap;
    line-height: 1;
  }
  .collection-title {
    font-family: "Marcellus", serif;
    font-size: 22px;
    letter-spacing: 0.6em;
    padding-left: 0.6em;
    color: var(--herb-green);
  }
  .collection-title.first { top: 291px; }
  .collection-title.second { top: 318px; }
  .herb-sprig {
    position: absolute;
    left: 522px;
    top: 362px;
    width: 208px;
    height: 172px;
    background: radial-gradient(closest-side, var(--leaf-brown) 0%, var(--leaf-plum) 60%, rgba(251,248,207,0) 100%);
    opacity: 0.8;
  }
  .brand-name {
    top: 537px;
    font-family: "Marcellus", serif;
    font-size: 63px;
    color: var(--herb-green);
  }
  .brand-descriptor {
    top: 613px;
    font-family: "Della Respira", serif;
    font-size: 35px;
    color: var(--bark-brown);
  }
  .slogan {
    top: 744px;
    font-family: "Marcellus", serif;
    font-size: 29px;
    letter-spacing: 0.4em;
    padding-left: 0.4em;
    color: var(--sage-green);
  }
</style>
</head>
<body>
<div class="canvas">
  <div class="label"></div>

  <svg class="label-lines" viewBox="0 0 1200 1000" aria-hidden="true">
    <path d="M153 735 V224 H1048 V735" fill="none" stroke="var(--gold-soft)" stroke-width="1.5"/>
    <circle cx="153" cy="735" r="5" fill="var(--gold-soft)"/>
    <circle cx="1048" cy="735" r="5" fill="var(--gold-soft)"/>
    <path d="M309 534 A287 287 0 0 1 883 534" fill="none" stroke="var(--gold)" stroke-width="2.5"/>
    <path d="M327 534 A269 269 0 0 1 865 534" fill="none" stroke="var(--gold-soft)" stroke-width="1"/>
    <circle cx="309" cy="534" r="5.5" fill="var(--gold)"/>
    <circle cx="883" cy="534" r="5.5" fill="var(--gold)"/>
    <circle cx="327" cy="534" r="2.5" fill="var(--gold)"/>
    <circle cx="865" cy="534" r="2.5" fill="var(--gold)"/>
    <line x1="407" y1="351" x2="789" y2="351" stroke="var(--gold-soft)" stroke-width="1"/>
    <line x1="148" y1="779" x2="1045" y2="779" stroke="var(--gold-soft)" stroke-width="1"/>
    <circle cx="148" cy="779" r="2.5" fill="var(--gold-soft)"/>
    <circle cx="1045" cy="779" r="2.5" fill="var(--gold-soft)"/>
  </svg>

  <div class="text-line collection-title first">HILLSIDE</div>
  <div class="text-line collection-title second">COLLECTION</div>

  <div class="herb-sprig" role="img" aria-label="Watercolour illustration of two crossed herb sprigs in brown and plum tones"></div>

  <div class="text-line brand-name">Meadowlark Remedies</div>
  <div class="text-line brand-descriptor">Apothecary &amp; Herb Farm</div>
  <div class="text-line slogan">TIMELESS HERBS FOR GENTLE LIVING</div>
</div>
</body>
</html>
```